New ProNexa (Personal and Business) Banner Design Project

The specifications for a new ProNexa banner are accessible online, and are not repeated here.

The background design for both banners will be the same, and must complement my business logo. The only difference between the banners will be the wording, although I'd prefer that both 'titles' and 'subscript' were written in the same size and colour of font.

I'm going to include a previous example of a banner I used, which was once perfect, but now lacks detail, as you can see.

My core brand is 'authentic leadership', and one suggestion of a new banner is that it contains the following words, written in such a way that they do not detract from the heading or subscript:

1. Authentic leadership
2. Integrity
3. Respect for others
4. Accountability
5. Sense of humour
6. Humility
7. Fairness
8. Truth to power
9. Question the Status Quo
10.Maverick
11.Transparency
12.Good governance
13.Regulation
14.Brandt Principles
15.Reflective learning
16.Continuous improvement
17.Growth mindset
18.Learning and development

I attach some examples for inspiration. The words can be written in any size, any direction, any font, any colour, and in any order, but must not detract from the logo, heading or subscript.

I also an example of someone else's work to demonstrate the differences. They are not perfect, and I'm looking for creativity, originality and innovation.

THANK YOU FOR YOUR INMITIAL DRAFTS, ALL OF WHICH REQUIRE MORE WORK. I HAVE ADDED MY BUSINESS LOGO AS A COLOUR GUIDE. IN ADDITION, PLEASE NOTE THAT I WOULD RATHER GET THIS RIGHT THAN RUSH IT. THE DEADLINE IS 5 WORKING DAYS FROM THE START DATE.

THANKS AGAIN.

Target Market(s)

I hope to generate most future business through ProNexa. Middle and senior managers will therefore access both my personal and business profiles to assess my competence. The designs are therefore targeted at professionals, rather than youth, low paid manual workers, or the unemployed.

Industry/Entity Type

Professional Service

Font styles to use
Sans Serif

Requirements
Must have
• The Business Banner must read:

1. Title. Professional Consultant, Coach, and Mentor
2. Subscript. "we exist to enable businesses and learners to achieve their potential"

The Personal Banner must read:

3. Title. Carrowmere Growth Partners Limited
4. Subscript. "in continuous pursuit of excellence with intellect and good humour"

Both banners must have the same backgrounds, and satisfy the prerequisite conditions outlined by ProNexa.com for publishing on desktop, laptop, tablet, and phone.

Neither banner must detract from the business logo, or make it difficult to read titles or subscript

Two different banners
Nice to have
• My original banner design was fair, but could not be added to.

The inclusion of the aforementioned words is highly desirable, although these need not to easy to read

The colour blue might work

Easy to search for on ProNexa

I attach three random pictures for interest, although these ARE NOT A TEMPLATE.
Should not have
• Must not detract from logo

Backgrounds must not make headings and subscripts difficult to read at a glance

Must not be the wrong size

I would rather not just see plain text, written horizontally and vertically, with no imagination.

```html
<!DOCTYPE html>
<html lang="en">
<head>
<meta charset="utf-8">
<title>Carrowmere Growth Partners Limited – Cover Banner Options</title>
<link rel="stylesheet" href="https://fonts.googleapis.com/css2?family=Jost:wght@400;500;600&family=Didact+Gothic&display=swap">
<style>
  :root{
    --sheet-bg:#cfe0ef;
    --label:#2a2a2a;
    --brand-blue:#1b6fc0;
    --brand-grey:#5a5a5c;
    --white:#ffffff;
    --word-light:rgba(225,238,250,.55);
    --word-soft:rgba(200,222,245,.5);
    --word-pale:rgba(80,140,210,.32);
    --sky:#f3eee5;
    --sand:#77756f;
  }
  *{margin:0;padding:0;box-sizing:border-box}
  html,body{width:1200px;height:737px;overflow:hidden;background:var(--sheet-bg)}
  body{position:relative;font-family:"Jost",sans-serif}

  .option-number{position:absolute;left:12px;font:500 17px "Jost",sans-serif;color:var(--label)}
  .option-number--one{top:26px}
  .option-number--two{top:390px}
  .sheet-caption{position:absolute;top:356px;left:0;width:1200px;text-align:center;font:600 28px "Jost",sans-serif;color:var(--label);letter-spacing:.5px}

  .banner{position:absolute;left:38px;width:1123px;height:280px;background:var(--white);box-shadow:0 5px 8px rgba(0,0,0,.35);overflow:hidden}
  .banner--one{top:48px}
  .banner--two{top:409px}

  .banner__panel{position:absolute;inset:0;clip-path:polygon(0 0,610px 0,540px 280px,0 280px)}
  .banner--one .banner__panel{background:linear-gradient(180deg,#f4f8fc 0%,#c9ddf1 30%,#4d8fd3 62%,#1f6ec0 100%)}
  .banner--two .banner__panel{background:linear-gradient(180deg,#1a6cc0 0%,#3f86d0 30%,#a9c9ea 60%,#eef4fb 85%,#ffffff 100%)}

  .banner__stripe{position:absolute;inset:0;background:var(--brand-blue);clip-path:polygon(618px 0,638px 0,566px 280px,543px 280px)}

  .banner__photo{position:absolute;inset:0;clip-path:polygon(638px 0,1123px 0,1123px 280px,566px 280px);
    background:linear-gradient(200deg,#fbf7ef 0%,var(--sky) 22%,#c9c4bb 40%,#9c9890 65%,var(--sand) 100%)}

  .quote{position:absolute;left:648px;top:12px;width:356px;text-align:center;font:400 26px/34px "Jost",sans-serif;color:var(--brand-blue);letter-spacing:-1px}
  .quote__mark{font-weight:600;font-size:26px;letter-spacing:0}

  .title{position:absolute;font-weight:500;text-transform:uppercase;white-space:nowrap}
  .banner--one .title{left:64px;top:16px;width:450px;text-align:center;font-size:40px;line-height:1.08;letter-spacing:-2px}
  .title__line--blue{color:var(--brand-blue);display:block}
  .title__line--grey{color:var(--brand-grey);display:block;margin-top:4px}
  .banner--two .title{left:30px;top:18px;color:var(--white);font-size:34px;line-height:41px;letter-spacing:-1.6px}

  .word{position:absolute;white-space:nowrap;font-family:"Didact Gothic",sans-serif;line-height:1}
  .word--vertical{writing-mode:vertical-rl;transform:rotate(180deg)}
  .banner--one .word{color:var(--word-light)}
  .banner--one .word--soft{color:var(--word-soft)}
  .banner--one .word--strong{color:rgba(255,255,255,.72)}
  .banner--two .word--upper{color:rgba(255,255,255,.42)}
  .banner--two .word--lower{color:var(--word-pale)}
  .word--stack{text-align:center;line-height:1.15;white-space:normal}
</style>
</head>
<body>

<span class="option-number option-number--one">1</span>

<section class="banner banner--one" aria-label="Banner option one">
  <div class="banner__panel"></div>
  <div class="banner__stripe"></div>
  <div class="banner__photo" role="img" aria-label="Photo of a man crouching on a sunlit beach drawing a line in the sand"></div>

  <h1 class="title">
    <span class="title__line--blue">Carrowmere Growth</span>
    <span class="title__line--grey">Partners Limited</span>
  </h1>

  <span class="word" style="left:46px;top:116px;font-size:24px;transform:rotate(-6deg);color:rgba(255,255,255,.7)">Authentic</span>
  <span class="word" style="left:44px;top:146px;font-size:22px;transform:rotate(-6deg);color:rgba(255,255,255,.65)">Leadership</span>
  <span class="word word--soft" style="left:162px;top:122px;font-size:15px;transform:rotate(10deg)">Transparency</span>
  <span class="word word--soft" style="left:160px;top:140px;font-size:34px;transform:rotate(8deg)">Good</span>
  <span class="word word--soft" style="left:162px;top:176px;font-size:16px;transform:rotate(10deg)">Governance</span>
  <span class="word" style="left:46px;top:176px;font-size:19px;transform:rotate(-5deg)">Integrity</span>
  <span class="word" style="left:46px;top:200px;font-size:19px;transform:rotate(-3deg)">Fairness</span>
  <span class="word word--vertical" style="left:122px;top:172px;font-size:11px">Humility</span>
  <span class="word word--vertical" style="left:142px;top:168px;font-size:11px">Accountability</span>
  <span class="word word--soft" style="left:162px;top:198px;font-size:18px;transform:rotate(8deg)">Regulation</span>
  <span class="word word--strong" style="left:46px;top:222px;font-size:14px">Truth To Power</span>
  <span class="word word--soft" style="left:176px;top:222px;font-size:20px">Brandt</span>
  <span class="word" style="left:47px;top:242px;font-size:20px">Maverick</span>
  <span class="word word--soft" style="left:162px;top:244px;font-size:19px;transform:rotate(6deg)">Principles</span>
  <span class="word word--vertical word--stack" style="left:272px;top:172px;font-size:12px">Continuous<br>Improvement</span>
  <span class="word" style="left:275px;top:132px;font-size:31px;color:rgba(60,130,205,.6)">Reflective Learning</span>
  <span class="word word--strong" style="left:351px;top:184px;font-size:20px">Growth mindset</span>
  <span class="word" style="left:316px;top:226px;font-size:15px">Learning and development</span>

  <p class="quote"><span class="quote__mark">“</span> in continuous pursuit of excellence with intellect and good humour <span class="quote__mark">”</span></p>
</section>

<h2 class="sheet-caption">COVER IMAGE</h2>

<span class="option-number option-number--two">2</span>

<section class="banner banner--two" aria-label="Banner option two">
  <div class="banner__panel"></div>
  <div class="banner__stripe"></div>
  <div class="banner__photo" role="img" aria-label="Photo of a man crouching on a sunlit beach drawing a line in the sand"></div>

  <h1 class="title">Carrowmere Growth<br>Partners Limited</h1>

  <span class="word word--upper" style="left:426px;top:30px;font-size:20px">Authentic</span>
  <span class="word word--upper" style="left:418px;top:52px;font-size:20px">Leadership</span>
  <span class="word word--upper word--vertical" style="left:560px;top:14px;font-size:13px">Accountability</span>
  <span class="word word--upper word--vertical" style="left:535px;top:63px;font-size:17px">Fairness</span>
  <span class="word word--upper" style="left:71px;top:103px;font-size:17px">Sense of humour</span>
  <span class="word word--upper" style="left:266px;top:105px;font-size:14px">Reflective learning</span>
  <span class="word word--upper" style="left:434px;top:98px;font-size:19px">Integrity</span>
  <span class="word word--upper" style="left:50px;top:134px;font-size:14px">Brandt Principles</span>
  <span class="word word--upper" style="left:210px;top:129px;font-size:20px">Question the Status Quo</span>
  <span class="word word--lower" style="left:478px;top:134px;font-size:20px">Humility</span>
  <span class="word word--lower word--vertical" style="left:26px;top:160px;font-size:23px">Respect</span>
  <span class="word word--lower word--vertical" style="left:52px;top:164px;font-size:18px">For Others</span>
  <span class="word word--lower word--stack" style="left:98px;top:162px;font-size:14px">Continuous<br>Improvement</span>
  <span class="word word--lower word--vertical" style="left:214px;top:160px;font-size:22px">Maverick</span>
  <span class="word word--lower" style="left:254px;top:159px;font-size:22px">Transparency</span>
  <span class="word word--upper" style="left:411px;top:162px;font-size:18px">Growth Mindset</span>
  <span class="word word--lower word--stack" style="left:96px;top:212px;font-size:15px">Learning And<br>Development</span>
  <span class="word word--lower" style="left:244px;top:202px;font-size:14px">Regulation</span>
  <span class="word word--lower" style="left:331px;top:191px;font-size:33px">Truth to power</span>
  <span class="word word--lower" style="left:262px;top:231px;font-size:31px">Good governance</span>

  <p class="quote"><span class="quote__mark">“</span> in continuous pursuit of excellence with intellect and good humour <span class="quote__mark">”</span></p>
</section>

</body>
</html>
```